依頼詳細
http://www.kobarinu.com/のトップページのリニューアルを考えており
そちらのご提案をいただきたいという業務内容です。
コンテンツはそのままで、デザインのみ作成していただきたいというものです。
コーティングなどはございません。
サイズなども特に指定はありません。
イラストレーターにて納品をお願いいたします。
ページ数
1ページ
希望イメージ
シンプル 複雑
単色 カラフル
暗い 明るい
日常 高級
遊び心 厳粛
未来的 伝統的
女性的 男性的
希望する色
青系
納品ファイル
• イラストレーター形式 (.ai)
補足説明
よろしくお願いいたします。
■ 選んだ理由

社内で選定し、一番イメージに近いものを採用させて頂きました。

■ 提案者全員のお礼・コメント

今回弊社のコンペにたくさんの応募をしていただき真に感謝しております。
どの作品も素晴らしいものばかりで、最後まで選定に時間が掛かりました。
また機会がございましたら是非みなさまのお力をお借りさせて下さい。
ありがとうございました。

```html
<!DOCTYPE html>
<html lang="ja">
<head>
<meta charset="utf-8">
<title>緑川コンクリート工業株式会社</title>
<link href="https://fonts.googleapis.com/css2?family=Noto+Sans+JP:wght@400;700&family=Noto+Serif+JP:wght@600&display=swap" rel="stylesheet">
<style>
:root{
  --blue:#1e6fc0;
  --blue-dark:#14508f;
  --orange:#f3a23a;
  --text:#333;
  --line:#d6dbe0;
  --grey-bg:#f1f1f1;
  --white:#fff;
}
*{margin:0;padding:0;box-sizing:border-box}
html,body{width:1200px;height:4352px;overflow:hidden}
body{position:relative;font-family:"Noto Sans JP",sans-serif;color:var(--text);background:var(--white)}
.abs{position:absolute}
.hero{left:0;top:0;width:1200px;height:832px;background:linear-gradient(180deg,#b9cbe0 0%,#6f8aa8 30%,#3d4f66 70%,#2a3444 100%)}
.hero-shade{left:0;top:0;width:1200px;height:832px;background:linear-gradient(90deg,rgba(40,52,70,.55),rgba(120,140,160,.15) 60%,rgba(50,60,75,.5))}
.brand{left:40px;top:30px;display:flex;align-items:center;gap:12px;font-size:30px;font-weight:700;color:var(--blue-dark)}
.brand-dot{width:34px;height:34px;border-radius:50%;background:var(--blue-dark)}
.contact-btn{left:928px;top:28px;width:144px;height:44px;background:var(--orange);color:var(--white);border-radius:4px;font-size:16px;display:flex;align-items:center;justify-content:center}
.nav{left:150px;top:104px;display:flex;gap:44px;font-size:17px;color:var(--white)}
.hero-copy{left:120px;top:284px;color:var(--white);font-size:30px;line-height:1.45;text-shadow:0 1px 4px rgba(0,0,0,.5)}
.hero-sub{left:120px;top:440px;color:var(--white);font-size:19px;line-height:1.6;text-shadow:0 1px 4px rgba(0,0,0,.5)}
.section-title{left:0;width:1200px;text-align:center;font-family:"Noto Serif JP",serif;font-weight:600;font-size:32px;color:#222}
.product-title{font-size:22px;font-weight:700;color:var(--blue);width:976px;left:112px;border-bottom:2px solid var(--line);padding-bottom:8px}
.product-title.right{text-align:right}
.photo{background:linear-gradient(135deg,#c9ccd0,#8e959c)}
.photo.water{background:linear-gradient(180deg,#b8d3ea,#6f9cbf 55%,#9aa7a0)}
.photo.rail{background:linear-gradient(135deg,#8a8070,#4d4a45 60%,#9a9488)}
.desc{font-size:15px;line-height:1.75;color:#444}
.more{display:block;color:var(--blue);font-size:14px;margin-top:8px}
.case-label{font-size:17px;font-weight:700;color:#333}
.case-label::before{content:"";display:inline-block;width:10px;height:10px;background:var(--text);margin-right:8px}
.thumbs{left:112px;width:976px;display:flex;gap:19px}
.thumb{width:180px;flex:0 0 180px}
.thumb .photo{height:110px}
.thumb p{font-size:14px;margin-top:14px;color:#444}
.divider{left:112px;width:976px;height:1px;background:var(--line)}
.news{left:0;top:2960px;width:1200px;height:520px;background:var(--grey-bg)}
.news-list{left:340px;top:3060px;width:520px;list-style:none;border-top:1px solid #bbb}
.news-list li{height:76px;border-bottom:1px solid #bbb;display:flex;align-items:center;gap:30px;padding-left:24px;font-size:16px}
.social-box{left:340px;top:3560px;width:520px;height:280px;border:1px solid #ccc;background:var(--white)}
.social-head{padding:16px;display:flex;gap:14px;align-items:center;font-size:16px;font-weight:700;color:var(--blue-dark)}
.social-head span{width:56px;height:56px;background:#e5e8ec;display:block}
.social-faces{display:flex;gap:8px;padding:8px 16px;flex-wrap:wrap}
.social-faces div{width:56px;height:56px;background:#cfd6de}
.banners{left:340px;top:3864px;width:520px;display:flex;gap:20px}
.banner{flex:1;height:136px;background:linear-gradient(135deg,#eef2f6,#c9d5e2);border:1px solid #ccd}
.footer{left:0;top:4100px;width:1200px;height:252px;background:var(--blue)}
.footer-info{left:0;top:4128px;width:1200px;text-align:center;color:var(--white);font-size:15px}
.footer-mark{left:574px;top:4184px;width:52px;height:52px;border-radius:50%;border:3px solid var(--white)}
.footer-name{left:0;top:4248px;width:1200px;text-align:center;color:var(--white);font-size:14px}
.copyright{left:0;top:4296px;width:1200px;height:56px;background:var(--blue-dark);color:#dfe9f5;font-size:13px;display:flex;align-items:center;justify-content:center}
</style>
</head>
<body>
<header>
  <div class="abs hero" role="img" aria-label="コンクリート製品が並ぶ工場ヤードの写真"></div>
  <div class="abs hero-shade"></div>
  <div class="abs brand"><span class="brand-dot"></span>緑川コンクリート工業株式会社</div>
  <a class="abs contact-btn">お問い合わせ</a>
  <nav class="abs nav"><span>トップページ</span><span>製品案内</span><span>施工事例</span><span>研究開発</span><span>検査分野</span><span>企業情報</span><span>採用情報</span><span>お問い合わせ</span></nav>
  <p class="abs hero-copy">コンクリートと共に創業50年。<br>これからも各種コンクリート製品のご提案を通して<br>地域に貢献できる会社を目指します。</p>
  <p class="abs hero-sub">緑川コンクリート工業株式会社は昭和39年創業以来、<br>石川県青葉市を拠点として各種コンクリート製品の<br>製造・販売・施工を行っています。</p>
</header>

<main>
  <h2 class="abs section-title" style="top:880px">製品情報</h2>

  <h3 class="abs product-title" style="top:952px">ロードスラブ（道路橋）</h3>
  <div class="abs photo" style="left:112px;top:1008px;width:448px;height:144px" role="img" aria-label="ロードスラブ製品の写真"></div>
  <div class="abs desc" style="left:600px;top:1004px;width:488px">近年、人件費の高騰による負担増、施工の効率化、製品の耐久性から、コンクリート構造物の工場製品化が進んでいます。ロードスラブは、実績値150以下の道路橋用に開発された鉄筋コンクリート・プレキャスト・プレストレストコンクリート床版です。強度、耐久性、施工性に優れ、短期間での架橋を可能にします。<a class="more">詳細はこちら</a></div>
  <p class="abs case-label" style="left:112px;top:1180px">施工事例</p>
  <div class="abs thumbs" style="top:1220px">
    <div class="thumb"><div class="photo" role="img" aria-label="車道タイプの施工写真"></div><p>車道タイプ</p></div>
    <div class="thumb"><div class="photo" role="img" aria-label="歩道タイプの施工写真"></div><p>歩道タイプ</p></div>
    <div class="thumb"><div class="photo" role="img" aria-label="農道タイプの施工写真"></div><p>農道タイプ</p></div>
    <div class="thumb"><div class="photo" role="img" aria-label="短スパン橋渡タイプの施工写真"></div><p>短スパン橋渡タイプ</p></div>
    <div class="thumb"><div class="photo" role="img" aria-label="管理橋タイプの施工写真"></div><p>管理橋タイプ</p></div>
  </div>
  <div class="abs divider" style="top:1420px"></div>

  <h3 class="abs product-title right" style="top:1460px">ガードライン</h3>
  <div class="abs desc" style="left:112px;top:1516px;width:488px">一般道において、車両の路面防止を目的に設けられた防護柵・ガードラインを開発致しました。豪雪時に変形しない剛性防護柵（リジッドタイプ）なので、雪害に強く、除雪作業にも適しています。車両の逸脱によって大きな二次災害が発生する恐れのある場所に適し、景観に配慮したデザインに仕上げております。<a class="more">詳細はこちら</a></div>
  <div class="abs photo" style="left:640px;top:1504px;width:448px;height:176px" role="img" aria-label="道路脇に設置されたガードラインの写真"></div>
  <p class="abs case-label" style="left:112px;top:1696px">施工事例</p>
  <div class="abs thumbs" style="top:1736px">
    <div class="thumb"><div class="photo" role="img" aria-label="車道タイプの施工写真"></div><p>車道タイプ</p></div>
    <div class="thumb"><div class="photo" role="img" aria-label="歩道タイプの施工写真"></div><p>歩道タイプ</p></div>
    <div class="thumb"><div class="photo" role="img" aria-label="農道タイプの施工写真"></div><p>農道タイプ</p></div>
    <div class="thumb"><div class="photo" role="img" aria-label="短スパン橋渡タイプの施工写真"></div><p>短スパン橋渡タイプ</p></div>
    <div class="thumb"><div class="photo" role="img" aria-label="管理橋タイプの施工写真"></div><p>管理橋タイプ</p></div>
  </div>
  <div class="abs divider" style="top:1940px"></div>

  <h3 class="abs product-title" style="top:1980px">コンクリートフロート（浮桟橋）</h3>
  <div class="abs photo water" style="left:112px;top:2036px;width:448px;height:144px" role="img" aria-label="水上に浮かぶコンクリート浮桟橋の写真"></div>
  <div class="abs desc" style="left:600px;top:2040px;width:488px">ボート用ステーハーバー、また、港トラックなどで外向けの主要に行くための乗降としても使用できます。また予約製品などにない大量の流れ、安定性の高さ、耐久性に優れ、海の生態系に配慮しています。<a class="more">詳細はこちら</a></div>
  <p class="abs case-label" style="left:112px;top:2200px">施工事例</p>
  <div class="abs thumbs" style="top:2240px">
    <div class="thumb"><div class="photo" role="img" aria-label="車道タイプの施工写真"></div><p>車道タイプ</p></div>
    <div class="thumb"><div class="photo" role="img" aria-label="歩道タイプの施工写真"></div><p>歩道タイプ</p></div>
    <div class="thumb"><div class="photo" role="img" aria-label="農道タイプの施工写真"></div><p>農道タイプ</p></div>
    <div class="thumb"><div class="photo" role="img" aria-label="短スパン橋渡タイプの施工写真"></div><p>短スパン橋渡タイプ</p></div>
    <div class="thumb"><div class="photo" role="img" aria-label="管理橋タイプの施工写真"></div><p>管理橋タイプ</p></div>
  </div>
  <div class="abs divider" style="top:2450px"></div>

  <h3 class="abs product-title right" style="top:2490px">鉄道関連製品</h3>
  <div class="abs desc" style="left:112px;top:2552px;width:488px">列車軌道の継ぎ目を必要とせず、短い施工期間で踏切線路を一新することが可能です。<a class="more">詳細はこちら</a></div>
  <div class="abs photo rail" style="left:648px;top:2544px;width:440px;height:156px" role="img" aria-label="線路と踏切ブロックの写真"></div>
  <p class="abs case-label" style="left:112px;top:2722px">施工事例</p>
  <div class="abs thumbs" style="top:2760px">
    <div class="thumb"><div class="photo" role="img" aria-label="車道タイプの施工写真"></div><p>車道タイプ</p></div>
    <div class="thumb"><div class="photo" role="img" aria-label="歩道タイプの施工写真"></div><p>歩道タイプ</p></div>
    <div class="thumb"><div class="photo" role="img" aria-label="農道タイプの施工写真"></div><p>農道タイプ</p></div>
    <div class="thumb"><div class="photo" role="img" aria-label="短スパン橋渡タイプの施工写真"></div><p>短スパン橋渡タイプ</p></div>
    <div class="thumb"><div class="photo" role="img" aria-label="管理橋タイプの施工写真"></div><p>管理橋タイプ</p></div>
  </div>

  <section>
    <div class="abs news"></div>
    <h2 class="abs section-title" style="top:2994px">新着情報</h2>
    <ul class="abs news-list">
      <li><span>2015年01月31日</span><span>ブログ更新しました。</span></li>
      <li><span>2015年01月31日</span><span>ブログ更新しました。</span></li>
      <li><span>2015年01月31日</span><span>ブログ更新しました。</span></li>
      <li><span>2015年01月31日</span><span>ブログ更新しました。</span></li>
    </ul>
  </section>

  <div class="abs social-box">
    <div class="social-head"><span></span>緑川コンクリート工業株式会社</div>
    <div class="social-faces">
      <div></div><div></div><div></div><div></div><div></div><div></div><div></div>
    </div>
  </div>
  <div class="abs banners">
    <div class="banner" role="img" aria-label="製品カタログのバナー"></div>
    <div class="banner" role="img" aria-label="新商品開発のバナー"></div>
    <div class="banner" role="img" aria-label="社員募集のバナー"></div>
  </div>
</main>

<footer>
  <div class="abs footer"></div>
  <p class="abs footer-info">〒920-0000 石川県青葉市緑町 12　電話 076-000-1234（代）FAX 076-000-5678</p>
  <div class="abs footer-mark"></div>
  <p class="abs footer-name">緑川コンクリート工業株式会社</p>
  <div class="abs copyright">© 2011-2014 Midorikawa Concrete Kogyo Co., Ltd.</div>
</footer>
</body>
</html>
```